Web Site Design For Real Estate Sales Project

The idea behind this project is pretty simple. I am putting my penthouse apartment up for sale and am trying to be creative in selling it.
Technically this will be pretty simple, it will be 3 pages but graphically this has to be as impressive as possible which is why I am trying Pixel Harbor.
The apartment is located in Barra Da Tijuca, Rio De Janeiro, Brazil. (This is where the 2016 Meridian Regatta will be held)
I am looking for an index page and 2 sub-pages. I am open to all kinds of designs and navigation's but it has to make an impression quickly with a professional and enticing design. The index page should make it obvious that there is a penthouse apartment for sale in Barra Da Tijuca ( suburb of Rio De Janeiro). The first sub page is about the Condominium where the apartment is located, the second sub page is about the apartment itself.
Here is a more detailed description of what the 3 pages should be about.
Index Page
This is the landing page and should make it obvious that there is an apartment for sale in Barra Da Tijuca, Rio De Janeiro with the following attributes
251 SQ M
Duplex Penthouse
4 suites
Price R$ 2.200.000
Price per SQ M: R$ 8.764
First Sub-Page
This is about the Condominium which is called "Gentle Palm Residences" with the following bullets
*Family friendly and safe
*Direct access to the beach
*Many amenities like pool, football court, gym, sauna
There should be some photos of the condominium and a link to the site of the condominium ( www.gprvx.com )
Second Sub-page
This is about the apartment. It should list in bullets the features of the apartment and then have a photo gallery of the view and various rooms. I have attached sample photos but will eventually have to use more photos.
Apartment Features
Price: R$ 2.220.000
251 m2 Duplex Penthouse
4 suites
maids room with bath
guest bathroom
living room
dinning room
Terrace with heated pool for year round use
Veranda
As mentioned above I am open to all designs and navigation so feel free to be creative. The important thing is catch peoples attention and get the message across in a few seconds, which is that there is an apartment for sale at this price with these features in this location. I will then use brightlist promoter and SEO to get people to the site.
Thanks
Target Market(s)
Men and Women from 30-60 years of age.
Industry/Entity Type
Apartment

```html
<!DOCTYPE html>
<html lang="en">
<head>
<meta charset="utf-8">
<title>Penthouse for sale in Barra Da Tijuca</title>
<link rel="stylesheet" href="https://fonts.googleapis.com/css2?family=Josefin+Slab:wght@400;600;700&family=Oswald:wght@400;500;700&display=swap">
<style>
  :root {
    --page-dark: #1e1e1e;
    --panel-grey: rgba(175, 175, 175, 0.72);
    --contact-grey: #a9a9a9;
    --ink: #3a3a3a;
    --ink-soft: #5e5e5e;
    --rule: #555555;
    --teal: #2a9a8e;
    --steel-blue: #3b7fa6;
    --white: #ffffff;
  }
  * { margin: 0; padding: 0; box-sizing: border-box; }
  html, body {
    width: 1200px;
    height: 747px;
    overflow: hidden;
    background: var(--page-dark);
  }
  .landing {
    position: relative;
    width: 1200px;
    height: 747px;
    background: var(--page-dark);
    overflow: hidden;
  }
  .hero-photo {
    position: absolute;
    left: 0;
    top: 29px;
    width: 1200px;
    height: 595px;
    background:
      linear-gradient(180deg, rgba(236,242,248,0.0) 0%, rgba(236,242,248,0) 100%),
      linear-gradient(160deg,
        #dfe9f2 0%, #c9dceb 18%, #7f98a8 30%,
        #2a6aa5 40%, #5b6f6a 55%, #8a8a80 66%,
        #4f6a45 80%, #2e4a26 100%);
  }
  .intro-panel {
    position: absolute;
    left: 26px;
    top: 0;
    width: 441px;
    height: 407px;
    background: var(--panel-grey);
    font-family: "Josefin Slab", serif;
    color: var(--ink);
    text-align: center;
  }
  .intro-panel .line { position: absolute; left: 0; width: 100%; white-space: nowrap; }
  .intro-panel strong { font-weight: 700; color: var(--ink); }
  .q1 { top: 40px; font-size: 38px; }
  .q2 { top: 96px; font-size: 26px; }
  .q3 { top: 138px; font-size: 38px; }
  .divider { position: absolute; left: 27px; top: 204px; }
  .s1 { top: 236px; font-size: 27px; color: var(--ink-soft); }
  .s2 { top: 272px; font-size: 44px; color: var(--ink-soft); }
  .s3 { top: 326px; font-size: 49px; }

  .contact-area {
    position: absolute;
    left: 25px;
    top: 646px;
    width: 442px;
    height: 101px;
    background: var(--contact-grey);
    font-family: "Josefin Slab", serif;
    font-size: 40px;
    color: var(--ink);
    text-align: center;
    line-height: 101px;
    letter-spacing: 0.5px;
  }

  .facts-panel {
    position: absolute;
    left: 734px;
    top: 424px;
    width: 441px;
    height: 323px;
    background: var(--panel-grey);
    font-family: "Oswald", sans-serif;
    color: var(--ink);
  }
  .facts-rule { position: absolute; left: 0; top: 0; }
  .badge {
    position: absolute;
    width: 118px;
    height: 118px;
    border-radius: 50%;
    color: var(--white);
    font-weight: 500;
    font-size: 24px;
    line-height: 28px;
    text-align: center;
    display: flex;
    flex-direction: column;
    justify-content: center;
    box-shadow: 2px 3px 6px rgba(0,0,0,0.35);
  }
  .badge-condo { left: 20px; top: 28px; background: var(--teal); }
  .badge-penthouse { left: 20px; top: 176px; background: var(--steel-blue); }
  .fact {
    position: absolute;
    left: 180px;
    font-size: 31px;
    white-space: nowrap;
    font-weight: 400;
    letter-spacing: 0.3px;
  }
  .f1 { top: 14px; }
  .f2 { top: 72px; }
  .f3 { top: 134px; }
  .f4 { top: 198px; }
  .f5 { top: 262px; }
  .fact b { font-weight: 700; }
</style>
</head>
<body>
<main class="landing">
  <div class="hero-photo" role="img" aria-label="Aerial photo of the Barra Da Tijuca coastline: blue ocean and curved beach, high-rise towers, lagoons and green mountains under a bright sky"></div>

  <section class="intro-panel">
    <p class="line q1">Looking for a <strong>home</strong></p>
    <p class="line q2">on the</p>
    <p class="line q3">Brazilian Coastline ?</p>
    <svg class="divider" width="390" height="12" viewBox="0 0 390 12" aria-hidden="true">
      <line x1="0" y1="6" x2="390" y2="6" stroke="var(--rule)" stroke-width="2"/>
      <circle cx="192" cy="6" r="6" fill="var(--rule)"/>
    </svg>
    <p class="line s1">There is a <strong>penthouse</strong> apartment</p>
    <p class="line s2">available now</p>
    <p class="line s3">in <strong>Barra Da Tijuca</strong></p>
  </section>

  <a class="contact-area">CONTACT AREA</a>

  <section class="facts-panel">
    <svg class="facts-rule" width="441" height="323" viewBox="0 0 441 323" aria-hidden="true">
      <line x1="158" y1="0" x2="158" y2="323" stroke="var(--rule)" stroke-width="2"/>
      <circle cx="158" cy="162" r="8" fill="var(--rule)"/>
    </svg>
    <div class="badge badge-condo"><span>THE</span><span>CONDO</span></div>
    <div class="badge badge-penthouse"><span>THE</span><span>PENTHOUSE</span></div>
    <p class="fact f1">251 sqm</p>
    <p class="fact f2">duplex penthouse</p>
    <p class="fact f3">4 suites</p>
    <p class="fact f4">$ 2.200.000</p>
    <p class="fact f5"><b>only</b> $ 8.764/sqm</p>
  </section>
</main>
</body>
</html>
```